Income Tax Flyer - Updates Needed

Just need to update this flyer design and give it a new look. We would like to keep all the same wording but make it stand out a little more. Our selling point is the "Same Day Tax Advance up to $6,000"

Industry/Entity Type

Lending, Small Loans, Tax Services, Title Loans, Personal Loans

```html
<!DOCTYPE html>
<html lang="en">
<head>
<meta charset="utf-8">
<title>Same Day Tax Advance Flyer</title>
<link rel="stylesheet" href="https://fonts.googleapis.com/css2?family=Oswald:wght@400;500;700&family=Roboto+Condensed:wght@400;700&display=swap">
<style>
  :root {
    --green: #1e5c3a;
    --green-dark: #17492e;
    --red: #d4212a;
    --ink: #4a4a4a;
    --paper: #ffffff;
    --muted: #6b6b6b;
  }
  * { margin: 0; padding: 0; box-sizing: border-box; }
  html, body { width: 849px; height: 1200px; overflow: hidden; background: var(--paper); }
  .flyer { position: relative; width: 849px; height: 1200px; background: var(--paper); overflow: hidden; font-family: "Roboto Condensed", sans-serif; }

  .hero-photo {
    position: absolute; left: 85px; top: 150px; width: 764px; height: 510px;
    background: linear-gradient(160deg, #f4f4f3 0%, #e7e6e3 40%, #d9d6d1 70%, #c9c4bc 100%);
  }

  .headline { position: absolute; left: 42px; top: 40px; font-family: "Oswald", sans-serif; color: var(--green); }
  .headline .lead { font-weight: 700; font-size: 58px; line-height: 66px; letter-spacing: 0.5px; }
  .headline .amount { font-weight: 700; font-size: 132px; line-height: 150px; color: var(--red); margin-left: 58px; }
  .swoosh { position: absolute; left: 60px; top: 290px; }

  .brand { position: absolute; left: 540px; top: 55px; width: 270px; text-align: center; font-family: "Oswald", sans-serif; font-weight: 500; color: var(--green); font-size: 40px; line-height: 44px; }

  .offer-panel { position: absolute; left: 0; top: 655px; width: 395px; height: 295px; background: var(--green); color: #fff; font-family: "Oswald", sans-serif; padding: 22px 0 0 42px; }
  .offer-panel .line { font-weight: 400; font-size: 50px; line-height: 62px; }
  .offer-panel .accent { font-weight: 700; font-size: 58px; line-height: 70px; }
  .panel-notch { position: absolute; left: 380px; top: 640px; }

  .features { position: absolute; left: 440px; top: 680px; list-style: none; }
  .feature { display: flex; align-items: center; height: 86px; margin-bottom: 4px; }
  .feature svg { flex: none; margin-right: 26px; }
  .feature span { font-size: 34px; line-height: 38px; color: var(--ink); }

  .addresses { position: absolute; left: 85px; top: 985px; list-style: none; font-size: 17px; color: var(--muted); }
  .addresses li { height: 56px; }

  .contact { position: absolute; left: 470px; top: 955px; width: 379px; text-align: center; font-family: "Oswald", sans-serif; }
  .contact .cta { font-weight: 700; font-size: 38px; color: var(--green); line-height: 48px; }
  .contact .phone { font-weight: 700; font-size: 46px; color: var(--red); line-height: 58px; }

  .footer-bar { position: absolute; left: 468px; top: 1160px; width: 381px; height: 40px; background: var(--green); }
</style>
</head>
<body>
<main class="flyer">
  <div class="hero-photo" role="img" aria-label="Photo of a professional woman working on a laptop at an office desk"></div>

  <h1 class="headline">
    <div class="lead">Same Day Tax</div>
    <div class="lead">Advance up to</div>
    <div class="amount">$6,000</div>
  </h1>
  <svg class="swoosh" width="340" height="30" viewBox="0 0 340 30" aria-hidden="true">
    <path d="M0 22 Q170 -8 340 22 Q170 6 0 22 Z" fill="var(--green)"/>
  </svg>

  <div class="brand">Ledgerline<br>Financial Group</div>

  <section class="offer-panel">
    <div class="line">File your</div>
    <div class="line">taxes and</div>
    <div class="line">apply for an</div>
    <div class="accent">Easy Advance</div>
  </section>
  <svg class="panel-notch" width="30" height="30" viewBox="0 0 30 30" aria-hidden="true">
    <path d="M0 15 L30 0 L15 30 Z" fill="var(--red)"/>
  </svg>

  <ul class="features">
    <li class="feature">
      <svg width="64" height="64" viewBox="0 0 64 64" aria-hidden="true">
        <circle cx="32" cy="32" r="28" fill="none" stroke="var(--green)" stroke-width="4"/>
        <text x="32" y="38" text-anchor="middle" font-family="Oswald, sans-serif" font-weight="700" font-size="18" fill="var(--red)">24/7</text>
      </svg>
      <span>Available in 24<br>Hours or less</span>
    </li>
    <li class="feature">
      <svg width="64" height="64" viewBox="0 0 64 64" aria-hidden="true">
        <circle cx="32" cy="32" r="28" fill="none" stroke="var(--green)" stroke-width="4"/>
        <text x="32" y="42" text-anchor="middle" font-family="Oswald, sans-serif" font-weight="700" font-size="28" fill="var(--green)">$</text>
      </svg>
      <span>Choose your<br>Loan Amount</span>
    </li>
    <li class="feature">
      <svg width="64" height="64" viewBox="0 0 64 64" aria-hidden="true">
        <circle cx="32" cy="32" r="28" fill="none" stroke="var(--green)" stroke-width="4"/>
        <path d="M20 33 L29 42 L45 22" fill="none" stroke="var(--red)" stroke-width="5" stroke-linecap="round" stroke-linejoin="round"/>
      </svg>
      <span>Quick and Easy</span>
    </li>
  </ul>

  <ul class="addresses">
    <li>Address XXXXX XXX XXX</li>
    <li>Address XXXXX XXX XXX</li>
    <li>Address XXXXX XXX XXX</li>
  </ul>

  <div class="contact">
    <div class="cta">Contact Us Today!</div>
    <div class="phone">(000) 123 4567 890</div>
  </div>

  <div class="footer-bar"></div>
</main>
</body>
</html>
```